New Electrical Business Card Design

I would like a new design for my business cards.
i would like the same logo and font but new design
Please see attached files for front and back design.
large image can be used for graphics.
I would like the instagram link incorporated to back of card.
website site address needs to be changed to www.kestrelvoltworks.au
everything else stays as is

```html
<!DOCTYPE html>
<html lang="en">
<head>
<meta charset="utf-8">
<title>Kestrel Voltworks – Business Cards</title>
<link href="https://fonts.googleapis.com/css2?family=Montserrat:wght@400;500;800&display=swap" rel="stylesheet">
<style>
  :root{
    --bg:#e6e6e4;
    --card-white:#ffffff;
    --brand-green:#06904a;
    --ink:#1e1e1e;
    --text:#333333;
    --soft-grey:#e3e3e5;
    --soft-green:rgba(255,255,255,.07);
  }
  *{box-sizing:border-box;margin:0;padding:0}
  html,body{width:1200px;height:786px;overflow:hidden}
  body{background:var(--bg);font-family:"Montserrat",sans-serif;position:relative}
  .card{position:absolute;top:238px;width:540px;height:310px;border-radius:4px;
        box-shadow:0 6px 18px rgba(0,0,0,.18);overflow:hidden}
  .card-front{left:40px;background:var(--card-white)}
  .card-back{left:620px;background:var(--brand-green)}

  .backdrop-graphic{position:absolute;border-radius:50%}
  .card-front .backdrop-graphic{width:300px;height:300px;right:-30px;top:20px;background:var(--soft-grey)}
  .card-back .backdrop-graphic{width:260px;height:260px;right:-40px;top:-70px;background:var(--soft-green)}

  .brand{font-weight:800;letter-spacing:-.5px;line-height:1;white-space:nowrap}
  .brand-name{font-size:28px;text-transform:uppercase}
  .brand-tag{font-size:10px;letter-spacing:1px;text-transform:uppercase;margin-top:4px;text-align:right}
  .card-front .brand{position:absolute;left:34px;top:38px;color:var(--ink);z-index:1}
  .card-front .brand-dot{display:inline-block;width:12px;height:12px;border-radius:50%;
        background:var(--brand-green);margin-left:8px;vertical-align:middle}

  .person{position:absolute;left:34px;top:118px;z-index:1}
  .person-name{font-weight:800;font-size:17px;color:var(--ink);text-transform:uppercase}
  .person-name .first{color:var(--brand-green)}
  .person-role{font-size:11px;color:var(--text);margin-top:3px}

  .details{position:absolute;left:34px;top:168px;font-size:11px;color:var(--text);line-height:1.35;z-index:1}
  .details .green{color:var(--brand-green)}
  .details .block{margin-bottom:10px}
  .contact{display:flex;align-items:center;gap:8px}
  .contact svg{width:10px;height:10px;fill:var(--brand-green);flex:none}

  .card-back .brand{position:absolute;left:50%;top:48%;transform:translate(-50%,-50%);color:#fff}
  .card-back .brand-name{font-size:38px}
  .card-back .brand-tag{font-size:12px}
  .social-link{position:absolute;left:0;right:0;bottom:26px;text-align:center;
        color:#fff;font-size:12px;font-weight:500;letter-spacing:.5px}
</style>
</head>
<body>
  <section class="card card-front" aria-label="Business card front">
    <div class="backdrop-graphic" role="img" aria-label="Large faint brand graphic"></div>
    <div class="brand">
      <div class="brand-name">Kestrel Voltworks<span class="brand-dot"></span></div>
      <div class="brand-tag">Electrical &amp; Data</div>
    </div>
    <div class="person">
      <div class="person-name"><span class="first">Daniel</span> Marrowby</div>
      <div class="person-role">CEO &amp; Founder</div>
    </div>
    <div class="details">
      <div class="block">
        <div><span class="green">ABN</span>- 61 208 447 913</div>
        <div><span class="green">Lic Number</span>- 518364c</div>
      </div>
      <div class="block">
        <div>14 TALLOWOOD Road,</div>
        <div>GLENMORE NSW</div>
      </div>
      <div class="contact">
        <svg viewBox="0 0 10 10"><path d="M2 0h2l1 3-1.5 1a6 6 0 0 0 2.5 2.5L7 5l3 1v2a2 2 0 0 1-2 2A8 8 0 0 1 0 2a2 2 0 0 1 2-2z"/></svg>
        <span>0412 583 906</span>
      </div>
      <div class="contact">
        <svg viewBox="0 0 10 10"><path d="M0 2h10v6H0z"/><path d="M0 2l5 3.5L10 2" fill="none" stroke="#fff" stroke-width="1"/></svg>
        <span>info@kestrelvoltworks.au</span>
      </div>
      <div class="contact">
        <svg viewBox="0 0 10 10"><circle cx="5" cy="5" r="5"/><path d="M0 5h10M5 0c-2.5 3-2.5 7 0 10M5 0c2.5 3 2.5 7 0 10" fill="none" stroke="#fff" stroke-width=".8"/></svg>
        <span>www.kestrelvoltworks.au</span>
      </div>
    </div>
  </section>

  <section class="card card-back" aria-label="Business card back">
    <div class="backdrop-graphic" role="img" aria-label="Faint brand graphic"></div>
    <div class="brand">
      <div class="brand-name">Kestrel Voltworks</div>
      <div class="brand-tag">Electrical &amp; Data</div>
    </div>
    <div class="social-link">instagram.com/kestrelvoltworks</div>
  </section>
</body>
</html>
```